Real Estate Entrepreneur needs a business card

I am a real estate entrepreneur, I buy houses for investment purposes, I act as a real estate agent representing buyers and sellers in residential home transactions, I am a contractor that does a wide range of home repairs and construction. I'd like a design that can stick with me through the years as my business grows and morphs to fit any niche I decide to pursue as markets change.

Target Market(s)

Anyone with interest that may be related to real estate.

Industry/Entity Type

Real Estate

Contact Information for Business Card

A card that stands out and doesn't put me in any one box. My business will evolve over time and I need a card that can stay relevant.

Colors

Designer to choose colors to be used in the design.

Requirements
Must have
• Character
Nice to have
• I'm open
Should not have
• Cliche houses and hammers

```html
<!DOCTYPE html>
<html lang="en">
<head>
<meta charset="utf-8">
<title>Reid Calder — Business Card</title>
<link href="https://fonts.googleapis.com/css2?family=Montserrat:wght@400;500;800&display=swap" rel="stylesheet">
<style>
  :root {
    --backdrop: #d5d8d9;
    --paper: #f7f7f7;
    --navy: #0b1423;
    --navy-deep: #050a14;
    --navy-glow: #1e2e45;
    --silver: #c9cdd2;
    --ink: #111111;
  }
  * { margin: 0; padding: 0; box-sizing: border-box; }
  html, body {
    width: 1200px; height: 1000px; overflow: hidden;
    background: var(--backdrop);
    font-family: "Montserrat", Arial, sans-serif;
  }
  .sheet {
    position: relative; width: 1200px; height: 1000px;
    display: flex; flex-direction: column; align-items: center; justify-content: center;
    gap: 60px;
  }
  .card {
    width: 700px; height: 400px; position: relative;
    box-shadow: 0 6px 18px rgba(0,0,0,0.15);
  }
  .card--front { background: var(--paper); }
  .front__identity { position: absolute; left: 56px; top: 120px; }
  .front__name {
    font-weight: 800; font-size: 46px; letter-spacing: 0.5px;
    color: var(--navy); line-height: 1;
  }
  .front__role {
    font-weight: 500; font-size: 14px; color: var(--ink); margin-top: 6px;
  }
  .front__contact {
    position: absolute; left: 56px; right: 40px; top: 232px;
    font-size: 17px; font-weight: 500; color: var(--ink);
  }
  .contact__line { display: flex; gap: 22px; white-space: nowrap; }
  .contact__line + .contact__line { margin-top: 10px; }
  .contact__web { margin-left: auto; }
  .card--back {
    background: radial-gradient(ellipse at 50% 50%, var(--navy-glow) 0%, var(--navy) 45%, var(--navy-deep) 100%);
    display: flex; align-items: center; justify-content: center;
  }
  .back__name {
    font-weight: 800; font-size: 56px; letter-spacing: 1px;
    color: var(--silver);
  }
</style>
</head>
<body>
  <main class="sheet">
    <section class="card card--front">
      <div class="front__identity">
        <h1 class="front__name">REID CALDER</h1>
        <p class="front__role">Real Estate Agent</p>
      </div>
      <div class="front__contact">
        <p class="contact__line">
          <span>T. 5550148XX</span>
          <span>F 5550192XX</span>
          <span>info@reidcalder.com</span>
          <span class="contact__web">www.reidcalder.com</span>
        </p>
        <p class="contact__line">4810 Birch Avenue NW. Halden AB T1R</p>
      </div>
    </section>
    <section class="card card--back">
      <p class="back__name">REID CALDER</p>
    </section>
  </main>
</body>
</html>
```